Leaflet to promote a new sports massage business

I am a Remedial and Sports Massage therapist and treat a range of people from professionals who spend hours working behind computers and have associated neck and back pain through poor posture to amateur sports people of varying intensity/ability - who encounter injuries along the way, or just need some good old stretching out.Remedial and sports massage helps people who have musculoskeletal injury, pain or dysfunction brought about by the stresses and strains of life. Through massage i can reduce pain, promote recovery after injury, relieve stress, and improve flexibility. All of this contributes to helping people feel better. I have just started working at a new location (address attached) and am looking to raise awareness that I am there and to promote the benefits of massage to encourage new clients(attached as a separate document). I have a business card (attached to the brief) which uses hands as the main device, I would like to include these – possibly in some sort of logo and I would like to use purple as a key colour (if colour is used). I also want to include the KVTB logo (attached) to add credibility

```html
<!DOCTYPE html>
<html lang="en">
<head>
<meta charset="utf-8">
<title>Harriet Lindqvist – Remedial and Sports Massage Leaflet</title>
<link href="https://fonts.googleapis.com/css2?family=Roboto+Condensed:wght@700;800&family=Source+Sans+3:wght@400;600&display=swap" rel="stylesheet">
<style>
  :root{
    --page:#e8e5e1;
    --paper:#ffffff;
    --panel-grey:#f0f0f2;
    --lilac:#9b5ba6;
    --plum:#5c0a55;
    --navy:#24307a;
    --cyan:#1a9ad6;
    --blue:#1a6fb5;
    --ink:#4a4a4a;
    --skin-light:#f3e6dc;
    --skin:#d9b49a;
    --photo-grey:#b9b2ad;
  }
  *{margin:0;padding:0;box-sizing:border-box;}
  html,body{width:1200px;height:964px;overflow:hidden;background:var(--page);}
  .leaflet{position:absolute;left:0;top:60px;width:1200px;height:845px;background:var(--paper);overflow:hidden;
    font-family:"Source Sans 3",sans-serif;box-shadow:0 4px 14px rgba(0,0,0,.18);}
  .shapes{position:absolute;inset:0;}
  .txt{position:absolute;white-space:nowrap;line-height:1;}

  .name{left:39px;top:61px;font-family:"Roboto Condensed",sans-serif;font-weight:800;font-size:69px;color:#fff;letter-spacing:1px;}
  .role{left:39px;top:151px;font-family:"Roboto Condensed",sans-serif;font-weight:700;font-size:35px;color:#fff;}

  .contact{right:31px;text-align:right;}
  .contact-label{top:32px;font-size:39px;color:var(--ink);}
  .contact-phone{top:73px;font-family:"Roboto Condensed",sans-serif;font-weight:700;font-size:55px;color:var(--ink);}
  .contact-email{top:135px;font-size:23px;color:#6a2a72;letter-spacing:.3px;}
  .contact-social{top:172px;font-size:20px;color:var(--ink);}

  .tagline{left:43px;top:247px;font-size:48px;color:var(--lilac);}
  .tagline-rule{position:absolute;left:41px;top:307px;width:562px;height:1.5px;background:var(--lilac);}
  .benefits-title{left:39px;top:325px;font-size:43px;color:var(--blue);}
  .benefits{position:absolute;left:39px;top:392px;list-style:none;}
  .benefits li{display:flex;align-items:center;height:39.3px;font-size:30px;color:var(--ink);}
  .benefits svg{width:26px;height:24px;margin-right:16px;flex:none;}

  .about{position:absolute;color:#fff;font-size:17px;line-height:1;}
  .about span{position:absolute;display:block;text-align:justify;text-align-last:justify;white-space:nowrap;}
  .about span.last{text-align-last:left;text-align:left;}

  .address{right:31px;text-align:right;color:#fff;}
  .address-label{top:466px;font-size:31px;}
  .address-venue{top:511px;font-size:41px;}
  .address-ground{top:570px;right:35px;font-weight:600;font-size:27px;}
  .address-street{top:606px;right:35px;font-weight:600;font-size:27px;}

  .credential{position:absolute;left:470px;top:722px;display:flex;align-items:center;gap:10px;}
  .credential-dot{width:22px;height:22px;border-radius:50%;background:var(--navy);}
  .credential-name{font-family:"Source Sans 3",sans-serif;font-weight:600;font-size:30px;color:var(--navy);letter-spacing:3px;}
</style>
</head>
<body>
<div class="leaflet">
  <svg class="shapes" width="1200" height="845" viewBox="0 0 1200 845">
    <defs>
      <linearGradient id="topBand" x1="0" x2="1" y1="0" y2="0">
        <stop offset="0" stop-color="#1f2a6e"/>
        <stop offset=".45" stop-color="#2d4aa0"/>
        <stop offset="1" stop-color="var(--cyan)"/>
      </linearGradient>
      <linearGradient id="massagePhoto" x1="0" x2="1" y1="0" y2="0">
        <stop offset="0" stop-color="#ffffff"/>
        <stop offset=".35" stop-color="var(--skin-light)"/>
        <stop offset="1" stop-color="var(--skin)"/>
      </linearGradient>
      <linearGradient id="backPhoto" x1="0" x2="1" y1="0" y2="0">
        <stop offset="0" stop-color="#9d9692"/>
        <stop offset="1" stop-color="#d8d3cf"/>
      </linearGradient>
    </defs>
    <rect class="contact-panel" x="0" y="0" width="1200" height="206" fill="var(--panel-grey)"/>
    <polygon class="top-band" points="0,0 789,0 770,37 0,37" fill="url(#topBand)"/>
    <polygon class="name-band" points="0,37 770,37 700,206 0,206" fill="var(--lilac)"/>
    <polygon class="about-panel" points="700,206 1200,206 1200,654 470,654" fill="var(--plum)"/>

    <rect class="footer-base" x="360" y="654" width="840" height="191" fill="var(--panel-grey)"/>
    <g role="img" aria-label="Photograph of a smiling woman receiving a shoulder massage">
      <polygon points="700,654 1200,654 1200,845 620,845" fill="url(#massagePhoto)"/>
    </g>
    <polygon class="logo-panel" points="469,666 736,666 658,823 396,823" fill="#ffffff"/>
    <g role="img" aria-label="Photograph of hands massaging a back">
      <polygon points="163,705 415,705 350,833 163,833" fill="url(#backPhoto)"/>
    </g>
    <g role="img" aria-label="Illustration of two overlapping purple hands">
      <polygon points="0,610 140,610 260,845 0,845" fill="var(--plum)"/>
    </g>

    <circle class="social-dot" cx="795" cy="184" r="14" fill="var(--navy)"/>
  </svg>

  <div class="txt name">HARRIET LINDQVIST</div>
  <div class="txt role">Remedial And Sports Massage Therapist</div>

  <div class="txt contact contact-label">Contact:</div>
  <div class="txt contact contact-phone">07700 900418</div>
  <div class="txt contact contact-email">harrietlindqvist@mailbox.net</div>
  <div class="txt contact contact-social">social: HarrietLindqvistMassage</div>

  <div class="txt tagline">Helping People Feel Better</div>
  <div class="tagline-rule"></div>
  <div class="txt benefits-title">Benefits of Massage</div>
  <ul class="benefits">
    <li><svg viewBox="0 0 26 24"><path d="M2 13 L9 20 L24 3" fill="none" stroke="var(--navy)" stroke-width="4"/></svg>Reduces pain</li>
    <li><svg viewBox="0 0 26 24"><path d="M2 13 L9 20 L24 3" fill="none" stroke="var(--navy)" stroke-width="4"/></svg>Promotes recovery</li>
    <li><svg viewBox="0 0 26 24"><path d="M2 13 L9 20 L24 3" fill="none" stroke="var(--navy)" stroke-width="4"/></svg>Improves posture and flexibility</li>
    <li><svg viewBox="0 0 26 24"><path d="M2 13 L9 20 L24 3" fill="none" stroke="var(--navy)" stroke-width="4"/></svg>Relieves stress</li>
    <li><svg viewBox="0 0 26 24"><path d="M2 13 L9 20 L24 3" fill="none" stroke="var(--navy)" stroke-width="4"/></svg>Improves health and wellbeing</li>
  </ul>

  <div class="about">
    <span style="left:709px;top:231px;width:460px;">I am a Remedial and Sports Massage therapist and treat a</span>
    <span style="left:697px;top:255px;width:472px;">range of people from professionals who spend hours working</span>
    <span style="left:685px;top:279px;width:484px;">behind computers and have associated neck and back pain</span>
    <span style="left:672px;top:304px;width:497px;">through poor posture to amateur sports people of varying</span>
    <span style="left:659px;top:328px;width:510px;">intensity/ability - who encounter injuries along the way, or just need</span>
    <span class="last" style="left:647px;top:351px;">some good old stretching out.</span>
    <span style="left:628px;top:388px;width:541px;">Remedial and sports massage helps people who have musculoskeletal</span>
    <span class="last" style="left:616px;top:412px;">injury, pain or dysfunction brought about by the stresses and strains of life.</span>
  </div>

  <div class="txt address address-label">New Address:</div>
  <div class="txt address address-venue">Stride Physiotherapy</div>
  <div class="txt address address-ground">Riverside Athletic Ground</div>
  <div class="txt address address-street">Elm Park Road, Ashbury, AB1 2CD</div>

  <div class="credential">
    <div class="credential-dot"></div>
    <div class="credential-name">KVTB</div>
  </div>
</div>
</body>
</html>
```